Innovative Webpage for leadership development and training company

Bright Harbor is a company supporting small organisations, in particular NGOs or projects, to increase the impact of their training and to increase the retention of talent through customized leadership development solutions. We help organisations to Grow Further & Coach Further
We want to have a simple but modern design webpage that stands outs from the usual consulting webpages
Here you are two possible examples of consulting firms approaching the same target audience
http://www.velmarquis.eu/
http://brovensite.com/#intro
The webpage should be designed and developed in a platform that allows full customization in the future both in terms of pages, text and images
It should allow the integration of two short videos that are currently under development
It should allow the maximum possible interoperabililty with tables and smartphones

Target Market(s)

Nonprofit, young professionals, technical assistance and capacity building projects, global SMEs, multicultural teals

Industry/Entity Type

Leadership

Number of Pages Required

5+ page

Requirements
Must have
• A dynamic/engaging/modern homepage
• A design that can be easily transferable to other pages
• A user-friendly platform that allows complete customization
• Evaluation Criteria
• 1. Overall Design/Feel of the webpage (in particular homepage). Our company looks for innovative leadership development and training. We often step out of our comfort zone in a playful positive way and that requires courage.
• 2. Flexibility to edit and/or translate homepage design to new/other pages
• 3. User-friendliness to customize, change the webpage
• 4. Completeness of coded pages (# of pages effectively developed)
Nice to have
• The maximum number of coded pages designed as per the attached file

```html
<!DOCTYPE html>
<html lang="en">
<head>
<meta charset="utf-8">
<title>Bright Harbor — Consulting, Training, Coaching</title>
<link href="https://fonts.googleapis.com/css2?family=Open+Sans:wght@300;400;600;700&display=swap" rel="stylesheet">
<style>
:root{
  --blue:#1b82c5;
  --orange:#f7941d;
  --gold:#f2b31b;
  --ink:#333;
  --muted:#777;
  --light:#ededed;
  --dark:#3a3a3a;
  --black:#151515;
  --cyan:#29a9e1;
  --white:#fff;
}
*{margin:0;padding:0;box-sizing:border-box}
html,body{width:1200px;height:3368px;overflow:hidden}
body{font-family:'Open Sans',sans-serif;color:var(--ink);background:var(--white);position:relative}
section,header,footer,nav{position:relative;width:1200px;overflow:hidden}
.brand{display:flex;align-items:center;gap:10px;font-weight:700;color:var(--blue);font-size:24px}
.brand-dot{width:22px;height:22px;border-radius:50%;background:var(--orange)}
/* nav */
.site-nav{height:52px;display:flex;align-items:center;justify-content:space-between;padding:0 60px 0 40px;background:var(--white)}
.site-nav .brand{font-size:20px}
.menu{display:flex;gap:26px;list-style:none;font-size:11px;color:#555}
.menu li.active{color:var(--white);background:var(--orange);padding:3px 9px;margin:-3px 0}
/* hero */
.hero{height:708px}
.hero-photo{position:absolute;inset:0;background:linear-gradient(120deg,#d9dde2 0%,#eef0f2 40%,#b7bcc3 75%,#8a8f96 100%)}
.hero-card{position:absolute;left:400px;top:330px;width:420px;padding:22px 26px;background:rgba(255,255,255,.93);border-left:6px solid var(--orange)}
.hero-card h1{font-weight:300;font-size:38px;color:var(--orange)}
.hero-card h1 b{font-weight:700;color:var(--blue);font-size:26px}
.hero-card h1 span{font-size:22px;color:#555}
.hero-card p{font-size:16px;color:#666;margin-top:6px;letter-spacing:1px}
/* welcome */
.welcome{height:120px;text-align:center;padding-top:30px}
.section-title{font-size:30px;font-weight:400;color:var(--blue)}
.section-title b{color:var(--orange);font-weight:700}
.section-title.o{color:var(--orange)}
.welcome p{font-size:12px;color:var(--muted);margin:10px auto 0;width:620px;line-height:1.5}
/* about */
.about{height:300px}
.about-text{position:absolute;left:160px;top:40px;width:400px}
.about-text h2{font-size:22px;color:var(--blue);font-weight:600}
.about-text h3{font-size:15px;font-weight:600;color:#444;margin-top:14px}
.about-text p{font-size:11px;color:var(--muted);line-height:1.6;margin-top:12px}
.btn{display:inline-block;background:var(--orange);color:var(--white);font-size:11px;padding:8px 18px;margin-top:18px}
.about-photo{position:absolute;left:600px;top:10px;width:440px;height:270px;background:linear-gradient(160deg,#4a5058,#1e2328)}
/* video */
.video-title{height:100px;text-align:center;padding-top:22px}
.video-title .section-title{color:var(--orange);font-weight:300}
.video{height:480px;background:linear-gradient(#3d3d3d 0 330px,#d9d9d9 330px)}
.video-frame{position:absolute;left:160px;top:55px;width:880px;height:330px;border:4px solid var(--gold);background:linear-gradient(135deg,#2e2e2e,#1c1c1c)}
.play{position:absolute;left:50%;top:50%;width:76px;height:50px;margin:-25px 0 0 -38px;background:var(--orange);border-radius:8px}
/* services */
.services{height:460px;background:var(--light);text-align:center;padding-top:50px}
.cards{position:absolute;left:160px;top:120px;display:flex;gap:20px}
.service-card{width:280px;height:280px;background:var(--white);text-align:left}
.service-photo{height:105px;background:linear-gradient(160deg,#cfd3d8,#7d848c)}
.service-card .body{padding:16px 14px;height:175px}
.service-card h4{font-size:13px;color:var(--orange);font-weight:600}
.service-card p{font-size:9.5px;color:var(--muted);line-height:1.5;margin-top:8px}
.service-card .more{font-size:9px;color:var(--orange);margin-top:12px;display:block}
.service-card.featured .body{background:var(--orange)}
.service-card.featured h4,.service-card.featured p,.service-card.featured .more{color:var(--white)}
/* clients */
.clients{height:380px;text-align:center;padding-top:70px}
.clients p{font-size:11px;color:var(--muted);width:560px;margin:8px auto 0;line-height:1.5}
.logo-strip{position:absolute;left:160px;top:190px;width:880px;height:150px;background:#f6f6f6;display:flex;align-items:center;justify-content:space-around}
.client{display:flex;align-items:center;gap:8px;font-size:17px;font-weight:600;color:#2c4f8a}
.client i{width:16px;height:16px;background:#2c4f8a;display:block}
.arrows{position:absolute;right:160px;top:172px;display:flex;gap:2px}
/* testimonials */
.testimonials{height:490px;background:var(--light);text-align:center;padding-top:70px}
.tcards{position:absolute;left:160px;top:168px;display:flex;gap:40px}
.tcard{width:267px;height:232px;background:var(--white);text-align:left;position:relative}
.tcard .quote{font-size:30px;color:var(--blue);line-height:1;padding:8px 14px 0;font-weight:700}
.tcard p{font-size:9.5px;color:#666;line-height:1.5;padding:0 18px}
.tcard .who{position:absolute;left:0;bottom:0;width:100%;height:78px;background:var(--blue);color:var(--white);padding:14px 16px 0 88px;font-size:9px;line-height:1.5}
.tcard .who b{display:block;font-size:10px}
.avatar{position:absolute;left:18px;top:-14px;width:56px;height:56px;border-radius:50%;border:3px solid var(--white);background:linear-gradient(#c9ced4,#8f969e)}
/* social */
.social{height:90px;display:flex;background:var(--dark)}
.social a{flex:1;display:flex;align-items:center;justify-content:center;gap:10px;color:#bbb;font-size:12px;text-decoration:none}
.social a.mid{background:var(--cyan);color:var(--white);flex:0 0 300px}
.social a i{width:10px;height:10px;border-radius:50%;background:currentColor;display:block}
/* footer */
.site-footer{height:188px;background:var(--black);text-align:center;padding-top:40px}
.site-footer .brand{justify-content:center;color:#666;font-size:22px}
.site-footer .brand-dot{background:#555}
.site-footer small{display:block;color:#555;font-size:10px;margin-top:40px}
</style>
</head>
<body>
<header class="site-nav">
  <div class="brand"><span class="brand-dot"></span>Bright Harbor</div>
  <ul class="menu">
    <li class="active">Home</li><li>About Us</li><li>Services</li><li>Testimonials</li><li>Blog</li><li>Contact Us</li>
  </ul>
</header>

<section class="hero">
  <div class="hero-photo" role="img" aria-label="Photo of a trainer presenting at a flip chart to a seated business team"></div>
  <div class="hero-card">
    <h1>Hello <b>Bright</b> <span>Harbor</span></h1>
    <p>Consulting · Training · Coaching</p>
  </div>
</section>

<section class="welcome">
  <h2 class="section-title">Welcome to <b>Bright</b> Harbor</h2>
  <p>Bright Harbor offers tailor-made leadership solutions for organisations and individual<br>professionals. We strive to grow further and coach further every day.</p>
</section>

<section class="about">
  <div class="about-text">
    <h2>About Us</h2>
    <h3>Mission Statement</h3>
    <p>We help small organisations, NGOs and projects increase the impact of their training and keep their best talent through customised leadership development, playful learning and honest coaching.</p>
    <span class="btn">Read More</span>
  </div>
  <div class="about-photo" role="img" aria-label="Photo of a confident business team standing together"></div>
</section>

<section class="video-title">
  <h2 class="section-title">View Our <b>Training Video</b></h2>
</section>

<section class="video">
  <div class="video-frame" role="img" aria-label="Training video player">
    <div class="play"><svg width="76" height="50" viewBox="0 0 76 50"><path d="M31 15 L49 25 L31 35 Z" fill="#fff"/></svg></div>
  </div>
</section>

<section class="services">
  <h2 class="section-title o">Our <b>Services</b></h2>
  <div class="cards">
    <article class="service-card featured">
      <div class="service-photo" role="img" aria-label="Photo of a team meeting around a table"></div>
      <div class="body"><h4>Organizational Development</h4><p>We help teams build shared purpose, clear roles and strong habits so the whole organisation learns and grows together over time.</p><span class="more">Learn More ›</span></div>
    </article>
    <article class="service-card">
      <div class="service-photo" role="img" aria-label="Photo of a coach talking with a professional"></div>
      <div class="body"><h4>Executive Coaching</h4><p>One-to-one coaching for leaders who want to step out of their comfort zone with courage and lead with more clarity.</p><span class="more">Learn More ›</span></div>
    </article>
    <article class="service-card">
      <div class="service-photo" role="img" aria-label="Photo of a workshop training session"></div>
      <div class="body"><h4>Training</h4><p>Practical, engaging workshops that turn skills into daily action and keep results alive long after the session ends.</p><span class="more">Learn More ›</span></div>
    </article>
  </div>
</section>

<section class="clients">
  <h2 class="section-title o">Our Clients</h2>
  <p>Non-profit organisations, young teams and global partners who trust us to<br>support their people and their mission.</p>
  <div class="arrows"><svg width="22" height="12" viewBox="0 0 22 12"><path d="M7 2 L3 6 L7 10 M15 2 L19 6 L15 10" stroke="#f7941d" stroke-width="2" fill="none"/></svg></div>
  <div class="logo-strip">
    <div class="client"><i></i>Meridian Civic Alliance</div>
    <div class="client">Lumen for Causes</div>
    <div class="client">Tallow Ridge</div>
    <div class="client">Clearpath Optics</div>
  </div>
</section>

<section class="testimonials">
  <h2 class="section-title">Testimonials</h2>
  <div class="tcards">
    <article class="tcard">
      <div class="quote">“</div>
      <p>I have been impressed by their capacity to read each team and design sessions that fit our needs. Our managers now run their own meetings with much more confidence and care.</p>
      <div class="who"><span class="avatar" role="img" aria-label="Client portrait"></span><b>Mr. Voss</b>Business Development Manager<br>Northfield Programme</div>
    </article>
    <article class="tcard">
      <div class="quote">“</div>
      <p>Their professionalism and dedication to the work is remarkable. The coaching helped our staff speak up, solve problems together and stay with us for longer.</p>
      <div class="who"><span class="avatar" role="img" aria-label="Client portrait"></span><b>Mr. Voss</b>Managing Director<br>Regional Support Office</div>
    </article>
    <article class="tcard">
      <div class="quote">“</div>
      <p>I have been impressed by their capacity to read each team and design sessions that fit our needs. Our managers now run their own meetings with much more confidence and care.</p>
      <div class="who"><span class="avatar" role="img" aria-label="Client portrait"></span><b>Mr. Voss</b>Business Development Manager<br>Northfield Programme</div>
    </article>
  </div>
</section>

<nav class="social">
  <a><i></i>Friendwall</a>
  <a class="mid"><i></i>Chirpline</a>
  <a><i></i>Circlecast</a>
</nav>

<footer class="site-footer">
  <div class="brand"><span class="brand-dot"></span>Bright Harbor</div>
  <small>© 2015 Bright Harbor. All rights reserved.</small>
</footer>
</body>
</html>
```